Business Card for Ferncliff Massage

I need a business card for my massage therapy & cannabis oil practice. I already have a logo,the "massage" got edited out of this file. I will send the original soon. I need these elements to be on the card:
web: FerncliffMassage.example
ph: 417/283-9061
email: Mirela.Dawkant@mailbox.example
Other slogans, statements to consider:
Science Geek, Massage Therapist, Neuromuscular Therapy, Cannabis Spa Treatments, Raindrop Therapy, Essential Oils
Target Market(s)
women between 20 & 65, people with enough $ to afford regular massage, people who recently had a motor vehicle accident, Halvora HMP insured
Industry/Entity Type
Massage Therapy
Contact Information for Business Card
I would like to see my bear logo featured; contact details, greens & blues preferred colors.

```html
<!DOCTYPE html>
<html lang="en">
<head>
<meta charset="utf-8">
<title>Ferncliff Massage — Business Card</title>
<link rel="stylesheet" href="https://fonts.googleapis.com/css2?family=Nunito:wght@400;600;700&family=Kalam:wght@400&display=swap">
<style>
  :root {
    --page: #eceeed;
    --card: #ffffff;
    --teal: #5aa98f;
    --teal-dark: #3f8f77;
    --sage: #7a8c68;
    --grey: #8a8d8b;
    --ink: #555a57;
  }
  * { box-sizing: border-box; margin: 0; padding: 0; }
  html, body {
    width: 882px; height: 1200px; overflow: hidden;
    background: var(--page);
    font-family: "Nunito", sans-serif;
  }
  .card {
    position: absolute; left: 81px;
    width: 720px; height: 411px;
    background: var(--card);
    box-shadow: 0 6px 18px rgba(0,0,0,0.12);
    overflow: hidden;
  }
  .card--front { top: 120px; }
  .card--back { top: 669px; }

  .brand {
    display: flex; align-items: center; gap: 14px;
    position: absolute;
  }
  .brand__dot {
    width: 30px; height: 30px; border-radius: 50%;
    background: var(--teal);
  }
  .brand__name {
    font-weight: 600; color: var(--sage);
    font-size: 52px; letter-spacing: 0.5px;
  }
  .card--front .brand { left: 50px; top: 150px; }
  .card--back .brand { left: 50%; top: 140px; transform: translateX(-50%); }
  .card--back .brand__name { font-size: 58px; }

  .contact {
    position: absolute; left: 370px; top: 36px; right: 36px;
    color: var(--teal-dark);
  }
  .contact__label {
    font-size: 13px; color: var(--grey); margin-left: 110px;
  }
  .contact__phone {
    font-family: "Kalam", cursive;
    font-size: 50px; line-height: 1.05; color: var(--teal-dark);
  }
  .contact__email {
    font-family: "Kalam", cursive;
    font-size: 20px; color: var(--teal-dark);
    margin-top: 2px; white-space: nowrap;
  }
  .divider {
    border: 0; border-top: 1px solid var(--teal);
    margin: 10px 0 12px; width: 100%;
  }
  .services {
    list-style: none; font-size: 12px; color: var(--grey);
    line-height: 1.6; columns: 2; column-gap: 18px;
  }

  .band {
    position: absolute; left: 0; right: 0; bottom: 0; height: 58px;
    background: var(--teal);
    display: flex; align-items: center; justify-content: center;
    color: #fff; font-size: 17px; letter-spacing: 4px;
  }
</style>
</head>
<body>
  <section class="card card--front">
    <div class="brand">
      <span class="brand__dot"></span>
      <span class="brand__name">Ferncliff</span>
    </div>
    <div class="contact">
      <p class="contact__label">Phone</p>
      <p class="contact__phone">417/283-9061</p>
      <p class="contact__label">Email</p>
      <p class="contact__email">Mirela.Dawkant@mailbox.example</p>
      <hr class="divider">
      <ul class="services">
        <li>Science Geek</li>
        <li>Massage Therapist</li>
        <li>Neuromuscular Therapy</li>
        <li>Cannabis Spa</li>
        <li>Raindrop Therapy</li>
        <li>Essential Oils</li>
      </ul>
    </div>
    <div class="band">www.ferncliffmassage.example</div>
  </section>

  <section class="card card--back">
    <div class="brand">
      <span class="brand__dot"></span>
      <span class="brand__name">Ferncliff</span>
    </div>
    <div class="band">www.ferncliffmassage.example</div>
  </section>
</body>
</html>
```